Design Challege - Simplify a Complex Message

We have a new website design, but one of the pages presents a particular problem.

Our company does ERP implementations. We have developed a proprietary approach to these implementations based on the idea that you must get eight (and only eight) things right. These eight things are listed below, summarized in one or two words each:

1. Value
2. Capability
3. Functionality
4. Data
5. Technology
6. Change Leadership
7. Quality
8. Governance

Each of these eight things can be summarized in a short paragraph, but when you combine all eight summaries with a brief introductory text, the result is a lot of text - so much text that the casual surfer may be overwhelmed by it.

The winning design will find an engaging way to present the information in a way that presents a high-level summary, using icons and one- or two-word descriptions above but revealing more information when clicked.

Our current design for this information, with a paragraph describing the eight elements in a table, is included as an upload in PDF and Microsoft Word formats. We are looking for a creative way to display these eight things, showing the detail only when the user wants to see it.

The website is being built in WordPress, using Elementor as a page builder.

We will implement (code) the page, but the winner will be asked to specify the widget or other add-in if one is required.

The design does not need to include a header or footer, we have those.

Target Market(s)

Business executives working in technology

Industry/Entity Type

Any

Number of Pages Required

1 page

Font styles to use
Sans Serif

Requirements
Must have
• A design for the body of the page, but not the header or footer.
Nice to have
• Unique icons or images appropriate for each of the eight things.
Should not have
• A lot of text on one page

```html
<!DOCTYPE html>
<html lang="en">
<head>
<meta charset="utf-8">
<title>ERP Implementations – 8 Things to Get Right</title>
<link href="https://fonts.googleapis.com/css2?family=Poppins:wght@400;500;600;700&display=swap" rel="stylesheet">
<style>
:root{
  --page-bg:#f5f4fc;
  --ink:#1f1f1f;
  --text:#4a4a4a;
  --muted:#5a5a5a;
  --brand:#22639b;
  --rule:#b9b9c0;
  --panel:#ffffff;
  --pill-idle:#ffffff;
  --pill-idle-text:#a8a8a8;
}
*{box-sizing:border-box;margin:0;padding:0}
html,body{width:1200px;height:999px;overflow:hidden}
body{background:var(--page-bg);font-family:"Poppins",sans-serif;color:var(--text);position:relative}

.variant-switch{position:absolute;top:24px;left:967px;display:flex;gap:8px}
.variant-switch span{height:22px;width:63px;border-radius:11px;background:var(--pill-idle);color:var(--pill-idle-text);font-size:10.5px;display:flex;align-items:center;justify-content:center}
.variant-switch .is-active{background:var(--brand);color:#fff}

.content{position:absolute;left:278px;top:86px;width:644px}
.eyebrow{font-size:17.5px;font-weight:400;color:var(--brand);line-height:24px}
.page-title{font-size:28px;font-weight:700;color:var(--ink);line-height:36px;margin-top:6px}
.intro{font-size:11px;line-height:20px;margin-top:47px;color:var(--text)}
.intro + .intro{margin-top:20px}
.intro strong{font-weight:600;color:var(--ink)}
.hint{display:flex;align-items:center;gap:6px;margin-top:18px;font-size:11px;font-weight:600;color:var(--muted)}

.accordion{margin-top:43px}
.acc-head{display:flex;justify-content:space-between;align-items:flex-end;height:47px;padding:0 0 3px 3px;border-bottom:1px solid var(--rule)}
.acc-head h2{font-size:17.5px;font-weight:500;color:var(--muted);line-height:24px}
.acc-head svg{margin-bottom:4px;margin-right:1px}
.acc-item.is-open .acc-head{height:30px}
.acc-item.is-open .acc-head h2{color:var(--brand)}
.acc-item.is-open .acc-head svg{margin-bottom:10px}
.acc-item.after-open .acc-head{height:42px}

.acc-panel{background:var(--panel);border-radius:0 0 8px 8px;height:164px;display:flex;padding:23px 20px 0 27px;gap:11px}
.value-icon{width:44px;height:44px;flex:none;margin-top:2px;background:var(--brand);border-radius:6px}
.acc-body p{font-size:11px;line-height:20px;color:var(--text)}
.learn-more{display:inline-flex;align-items:center;gap:6px;margin-top:14px;font-size:11px;font-weight:600;color:var(--brand);text-decoration:none}
</style>
</head>
<body>
<nav class="variant-switch">
  <span>Option 1</span><span class="is-active">Option 2</span><span>Option 3</span>
</nav>

<main class="content">
  <p class="eyebrow">ERP Implementations</p>
  <h1 class="page-title">8 Things to Get Right</h1>
  <p class="intro">Like the roots and branches of a tree, there are many considerations in an ERP implementation. Focus too much on the minor details, and you can lose sight of the tree.</p>
  <p class="intro">In an ERP implementation, you must get <strong>eight major things</strong> right to be successful. Ignore any of them, and your implementation will fail. Get them right, and you will likely succeed.</p>
  <p class="hint">
    <svg width="21" height="21" viewBox="0 0 21 21"><circle cx="10.5" cy="10.5" r="10.5" fill="#555"/><circle cx="11.6" cy="5.4" r="1.5" fill="#fff"/><path d="M10 8.6h2.2l-1.5 7.6H8.6z" fill="#fff"/></svg>
    Click the points below to read its description.
  </p>

  <section class="accordion">
    <div class="acc-item is-open">
      <div class="acc-head"><h2>1. Value</h2>
        <svg width="10" height="14" viewBox="0 0 10 14"><path d="M2 2l5 5-5 5" fill="none" stroke="#555" stroke-width="2.4"/></svg></div>
      <div class="acc-panel">
        <div class="value-icon" role="img" aria-label="Icon of a hand holding a diamond"></div>
        <div class="acc-body">
          <p>The project must provide value that significantly exceeds potential project costs and should be aligned with the company's strategy. Its value and strategic alignment must be part of a vision shared by the company's leadership. Value from the project must be delivered in a way that respects resource constraints.</p>
          <a class="learn-more" href="#">Learn More
            <svg width="12" height="10" viewBox="0 0 12 10"><path d="M1 5h9M6 1l4 4-4 4" fill="none" stroke="currentColor" stroke-width="1.5"/></svg></a>
        </div>
      </div>
    </div>
    <div class="acc-item after-open"><div class="acc-head"><h2>2. Capability</h2><svg width="14" height="10" viewBox="0 0 14 10"><path d="M2 2l5 5 5-5" fill="none" stroke="#555" stroke-width="2.4"/></svg></div></div>
    <div class="acc-item"><div class="acc-head"><h2>3. Functionality</h2><svg width="14" height="10" viewBox="0 0 14 10"><path d="M2 2l5 5 5-5" fill="none" stroke="#555" stroke-width="2.4"/></svg></div></div>
    <div class="acc-item"><div class="acc-head"><h2>4. Data</h2><svg width="14" height="10" viewBox="0 0 14 10"><path d="M2 2l5 5 5-5" fill="none" stroke="#555" stroke-width="2.4"/></svg></div></div>
    <div class="acc-item"><div class="acc-head"><h2>5. Technology</h2><svg width="14" height="10" viewBox="0 0 14 10"><path d="M2 2l5 5 5-5" fill="none" stroke="#555" stroke-width="2.4"/></svg></div></div>
    <div class="acc-item"><div class="acc-head"><h2>6. Change Leadership</h2><svg width="14" height="10" viewBox="0 0 14 10"><path d="M2 2l5 5 5-5" fill="none" stroke="#555" stroke-width="2.4"/></svg></div></div>
    <div class="acc-item"><div class="acc-head"><h2>7. Quality</h2><svg width="14" height="10" viewBox="0 0 14 10"><path d="M2 2l5 5 5-5" fill="none" stroke="#555" stroke-width="2.4"/></svg></div></div>
    <div class="acc-item"><div class="acc-head"><h2>8. Governance</h2><svg width="14" height="10" viewBox="0 0 14 10"><path d="M2 2l5 5 5-5" fill="none" stroke="#555" stroke-width="2.4"/></svg></div></div>
  </section>
</main>
</body>
</html>
```